Marisol transparent business card

I would like to have a transparent business card created.
A simple yet classy card with
Website www.MarisolPennington.example
Phone # 555-214-7396
I would like my full photo on the card as well as my logo.

Target Market(s)

The business card will be printed on transparent card stock.
Www.MarisolPennington.example
Phone 555-214-7396
I would like my pic on the card and my logo
Author, Speaker, & Wealth architect

Industry/Entity Type

Business

Contact Information for Business Card

Www.MarisolPennington.example
Phone 555-214-7396

Font styles to use
Serif
Decorative
Script

Requirements
Must have
• The business card will be printed on transparent card stock.
• Www.MarisolPennington.example
• Phone 555-214-7396
• I would like my pic on the card and my logo
• Author, Speaker, & Wealth architect
Nice to have
• If I could have the tattoo on my pic blurred out or airbrushed over

```html
<!DOCTYPE html>
<html lang="en">
<head>
<meta charset="utf-8">
<title>Marisol Pennington – Transparent Business Card</title>
<link rel="stylesheet" href="https://fonts.googleapis.com/css2?family=Cinzel:wght@500&family=Questrial&display=swap">
<style>
  :root {
    --backdrop: #d9d2c8;
    --card-frost: rgba(246, 244, 240, 0.78);
    --card-edge: rgba(255, 255, 255, 0.9);
    --gold: #b8862a;
    --gold-deep: #7a4a0c;
    --gold-bright: #e3a834;
    --ink-dark: #2b2622;
    --role-blush: #f7d4c6;
    --contact-white: #fffaf2;
    --swoosh-black: #111111;
  }
  html, body {
    margin: 0;
    width: 1200px;
    height: 969px;
    overflow: hidden;
    background: var(--backdrop);
  }
  .canvas {
    position: relative;
    width: 1200px;
    height: 969px;
  }
  .card {
    position: absolute;
    left: 360px;
    top: 64px;
    width: 480px;
    height: 840px;
    border-radius: 20px;
    background: var(--card-frost);
    box-shadow: 0 0 0 1px var(--card-edge) inset, 0 18px 40px rgba(60, 45, 30, 0.18);
    overflow: hidden;
  }
  .card-art {
    position: absolute;
    inset: 0;
  }
  .brand {
    position: absolute;
    top: 30px;
    left: 0;
    width: 100%;
    text-align: center;
  }
  .brand-dot {
    display: block;
    width: 66px;
    height: 66px;
    margin: 0 auto 14px;
    border-radius: 50%;
    background: var(--gold);
  }
  .brand-name {
    margin: 0;
    font-family: "Cinzel", serif;
    font-weight: 500;
    font-size: 30px;
    line-height: 1;
    color: var(--gold);
  }
  .tagline {
    margin: 8px 0 0;
    font-family: "Cinzel", serif;
    font-size: 11px;
    letter-spacing: 0.4px;
    color: var(--ink-dark);
  }
  .roles {
    position: absolute;
    right: 28px;
    top: 562px;
    margin: 0;
    font-family: "Questrial", sans-serif;
    font-size: 22px;
    line-height: 34px;
    text-align: right;
    color: var(--role-blush);
  }
  .contacts {
    position: absolute;
    right: 28px;
    top: 684px;
    margin: 0;
    padding: 0;
    list-style: none;
    font-family: "Questrial", sans-serif;
    font-size: 18px;
    line-height: 34px;
    text-align: right;
    color: var(--contact-white);
  }
  .social-mark {
    display: inline-block;
    width: 16px;
    height: 16px;
    margin-left: 8px;
    vertical-align: -2px;
    background: rgba(255, 250, 242, 0.75);
    border-radius: 2px;
  }
</style>
</head>
<body>
<main class="canvas">
  <article class="card">
    <svg class="card-art" width="480" height="840" viewBox="0 0 480 840" aria-hidden="false">
      <defs>
        <linearGradient id="portraitTone" x1="0" y1="0" x2="0" y2="1">
          <stop offset="0" stop-color="#b79b86"/>
          <stop offset="0.35" stop-color="#3a2a22"/>
          <stop offset="1" stop-color="#151212"/>
        </linearGradient>
        <linearGradient id="goldSweep" x1="1" y1="0" x2="0.2" y2="1">
          <stop offset="0" stop-color="var(--gold-bright)"/>
          <stop offset="0.45" stop-color="#c98a22"/>
          <stop offset="0.8" stop-color="var(--gold-deep)"/>
          <stop offset="1" stop-color="#c9912c"/>
        </linearGradient>
      </defs>
      <rect class="portrait" x="0" y="196" width="372" height="644" fill="url(#portraitTone)" opacity="0.9" role="img" aria-label="Full-length portrait photo of Marisol Pennington, arms crossed, in a black dress"/>
      <path class="swoosh-edge" d="M480,178 C418,230 360,420 278,612 C226,738 118,818 0,842 L0,840 C110,812 214,730 262,612 C340,420 400,226 480,186 Z" fill="var(--swoosh-black)"/>
      <path class="gold-sweep" d="M480,192 C420,236 362,424 284,614 C234,738 128,820 14,840 L480,840 Z" fill="url(#goldSweep)"/>
    </svg>

    <header class="brand">
      <span class="brand-dot"></span>
      <h1 class="brand-name">Marisol Pennington</h1>
      <p class="tagline">LIVE YOUR LIFE ON PURPOSE, NO EXCUSES</p>
    </header>

    <p class="roles">Author<br>Speaker<br>&amp; Wealth architect</p>

    <ul class="contacts">
      <li>P : 555-214-7396</li>
      <li>Info@MarisolPennington.example</li>
      <li>www.MarisolPennington.example</li>
      <li>MarisolPennington.example<span class="social-mark"></span></li>
    </ul>
  </article>
</main>
</body>
</html>
```